VoIP Postcard - New customer prospects

Need a postcard that gets our brand in front of the locals. We are an established IT company that has been in business for 20 years. We need to put a campaign in front of local businesses to let then know what we do. You can see our info at brightlinkvoice.com. We currently do not have a logo for our branded BrightlinkVoice VoIP service, which is part of Copper Harbor Networks.

Target Market(s)

Business Owners

Industry/Entity Type

Business

Colors
0355a3
3276b5
33a6d7
ec1f27
f04a50

```html
<!DOCTYPE html>
<html lang="en">
<head>
<meta charset="utf-8">
<title>BrightlinkVoice Postcard</title>
<link rel="stylesheet" href="https://fonts.googleapis.com/css2?family=Roboto+Condensed:wght@400&family=Roboto:wght@400&display=swap">
<style>
  :root {
    --panel: #000000;
    --paper: #ffffff;
    --accent: #f7c21a;
    --text-light: #ffffff;
    --ink: #000000;
    --device: #2e3236;
    --device-light: #d9dadb;
    --contact-tile: #1f3447;
    --sky: #c9d3e0;
    --ridge: #3d56b8;
    --valley: #26306a;
  }
  * { margin: 0; padding: 0; box-sizing: border-box; }
  html, body { width: 1200px; height: 930px; overflow: hidden; background: var(--paper); }
  .postcard { position: relative; width: 1200px; height: 930px; background: var(--paper); font-family: "Roboto", Arial, sans-serif; }

  .promo-panel { position: absolute; left: 0; top: 0; width: 606px; height: 930px; background: var(--panel); color: var(--text-light); }
  .headline { position: absolute; left: 30px; top: 56px; font-family: "Roboto Condensed", "Arial Narrow", sans-serif; font-weight: 400; font-size: 36px; line-height: 49px; color: var(--accent); }
  .intro { position: absolute; left: 30px; top: 173px; width: 483px; font-size: 19px; line-height: 30px; text-align: justify; letter-spacing: 0.2px; }

  .product-shot { position: absolute; left: 30px; width: 198px; height: 97px; background: linear-gradient(160deg, var(--device-light) 0%, #8b8e91 35%, var(--device) 60%, #15181a 100%); }
  .shot-1 { top: 440px; }
  .shot-2 { top: 554px; background: linear-gradient(160deg, var(--device) 0%, #4a5055 45%, #1b1e20 100%); }
  .shot-3 { top: 667px; background: linear-gradient(180deg, #3a3f44 0%, var(--device) 50%, #1b1e20 100%); }

  .features { position: absolute; left: 243px; top: 456px; font-size: 20px; line-height: 30px; }
  .features-title { color: var(--accent); font-size: 20px; line-height: 30px; }
  .feature-list { list-style: none; }
  .feature-list li::before { content: "\2022"; margin-right: 8px; }

  .contact { position: absolute; left: 30px; top: 795px; width: 395px; text-align: center; color: var(--accent); font-size: 20px; line-height: 28px; }

  .contact-art { position: absolute; left: 445px; top: 766px; width: 135px; height: 135px; background: radial-gradient(circle at 50% 60%, #2c5a7a 0%, var(--contact-tile) 60%); }

  .address-side .stamp-box { position: absolute; left: 1034px; top: 29px; width: 137px; height: 183px; border: 2px solid var(--ink); }
  .to-label { position: absolute; left: 683px; top: 246px; font-family: "Roboto", Arial, sans-serif; font-size: 56px; line-height: 60px; color: var(--ink); }
  .address-line { position: absolute; left: 690px; width: 429px; height: 3px; background: var(--ink); }
  .line-1 { top: 335px; }
  .line-2 { top: 407px; }
  .line-3 { top: 485px; }

  .scenery { position: absolute; left: 606px; top: 766px; width: 594px; height: 164px; background: linear-gradient(180deg, var(--sky) 0%, #8fa0d0 25%, var(--ridge) 55%, var(--valley) 100%); }
</style>
</head>
<body>
<main class="postcard">
  <section class="promo-panel">
    <h1 class="headline">Discover our phone products<br>Our service beats all the rest</h1>
    <p class="intro">Our service comes equipped with many features that come right out of the box if you want to set them up. Many services out there will charge to have additional features on top of the service you already pay for. Here, we believe that these are included in the price of your service. We enjoy our service that much and want you to be able to appreciate it as well. Here is a list of all of the features we currently can provide for you.</p>

    <div class="product-shot shot-1" role="img" aria-label="Desk IP phone shown from the side"></div>
    <div class="product-shot shot-2" role="img" aria-label="Desk IP phone with colour display"></div>
    <div class="product-shot shot-3" role="img" aria-label="Desk IP phone keypad close-up"></div>

    <div class="features">
      <h2 class="features-title">Features:</h2>
      <ul class="feature-list">
        <li>Unlimited extensions</li>
        <li>Voicemail to email</li>
        <li>Company Directory</li>
        <li>Unlimited Auto Attendants</li>
        <li>Caller ID</li>
        <li>Voicemail</li>
        <li>Music On Hold</li>
        <li>Unlimited Paging and intercom groups</li>
        <li>Call Flow Control</li>
      </ul>
    </div>

    <div class="contact">
      <p>Contact us</p>
      <p>www.brightlinkvoice.com | Ph: 5550147820</p>
      <p>info@brightlinkvoice.com</p>
    </div>

    <div class="contact-art" role="img" aria-label="Contact us illustration with telephone and communication icons"></div>
  </section>

  <section class="address-side">
    <div class="stamp-box"></div>
    <p class="to-label">To</p>
    <div class="address-line line-1"></div>
    <div class="address-line line-2"></div>
    <div class="address-line line-3"></div>
  </section>

  <div class="scenery" role="img" aria-label="Mountain range landscape under a pale sky"></div>
</main>
</body>
</html>
```